TWL Business Card Design Project

Real Estate Broker, Realtor
I would like something similar to what I have attached from Corvell Realty except my company is Marlow Realty Group, LLC. Instead of a single "M" on the back I would like "TWL". Phone # 816-552-4917
Name - Dorian Faulk
Licensed in the State of Missouri
No address
email - dfaulk@marlowhomesexample.com
Contact Information for Business Card
I would like something similar to what I have attached from Corvell Realty except my company is Marlow Realty Group, LLC. Instead of a single "M" on the back I would like "TWL". Phone # 816-863-8328Name - Jeremy YiLicensed in the State of MissouriNo addressemail - dfaulk@marlowhomesexample.com

```html
<!DOCTYPE html>
<html lang="en">
<head>
<meta charset="utf-8">
<title>Marlow Realty Group, LLC — Business Card</title>
<link rel="stylesheet" href="https://fonts.googleapis.com/css2?family=Libre+Franklin:wght@600;700;800&display=swap">
<style>
  :root {
    --sky: #4aaedb;
    --umber: #4d4741;
    --paper: #ffffff;
    --stage: #2e2e30;
    --ink: #4a443e;
  }
  * { margin: 0; padding: 0; box-sizing: border-box; }
  html, body { width: 1200px; height: 660px; overflow: hidden; }
  body {
    background: var(--stage);
    font-family: "Libre Franklin", Arial, sans-serif;
    display: flex;
    align-items: center;
    justify-content: center;
    gap: 40px;
  }
  .card {
    position: relative;
    width: 520px;
    height: 297px;
    overflow: hidden;
    box-shadow: 0 10px 30px rgba(0,0,0,.45);
  }
  .card-front {
    background: var(--sky);
    display: flex;
    align-items: center;
    justify-content: center;
  }
  .wordmark {
    color: var(--umber);
    font-weight: 800;
    text-align: center;
    line-height: 1;
  }
  .wordmark .initials { display: block; font-size: 96px; letter-spacing: 4px; }
  .wordmark .company { display: block; font-size: 21px; margin-top: 6px; }

  .card-back { background: var(--paper); }
  .back-bands { position: absolute; inset: 0; }
  .back-wordmark {
    position: absolute;
    left: 32px;
    top: 36px;
    color: var(--paper);
    text-align: left;
  }
  .back-wordmark .initials { font-size: 58px; letter-spacing: 3px; }
  .back-wordmark .company { font-size: 14px; margin-top: 5px; }

  .contact {
    position: absolute;
    left: 232px;
    top: 152px;
    color: var(--ink);
    font-weight: 700;
  }
  .contact .agent-name { font-size: 22px; font-weight: 800; margin-bottom: 8px; }
  .contact .line {
    display: flex;
    align-items: center;
    gap: 7px;
    font-size: 13.5px;
    margin-bottom: 5px;
  }
  .contact .line svg { width: 13px; height: 13px; flex: none; }
  .contact .license { font-size: 13.5px; margin-top: 2px; }
</style>
</head>
<body>

  <section class="card card-front" aria-label="Card front">
    <div class="wordmark">
      <span class="initials">TWL</span>
      <span class="company">Marlow Realty Group, LLC</span>
    </div>
  </section>

  <section class="card card-back" aria-label="Card back">
    <svg class="back-bands" viewBox="0 0 520 297" preserveAspectRatio="none" aria-hidden="true">
      <polygon points="0,0 520,0 520,80 0,166" fill="var(--umber)"/>
      <polygon points="0,166 520,80 520,94 0,180" fill="var(--sky)"/>
    </svg>

    <div class="wordmark back-wordmark">
      <span class="initials">TWL</span>
      <span class="company">Marlow Realty Group, LLC</span>
    </div>

    <div class="contact">
      <p class="agent-name">Dorian Faulk</p>
      <p class="line">
        <svg viewBox="0 0 14 14" aria-hidden="true">
          <rect x="3" y="1" width="8" height="12" rx="1.5" fill="none" stroke="var(--sky)" stroke-width="1.6"/>
          <line x1="6" y1="11" x2="8" y2="11" stroke="var(--sky)" stroke-width="1.4"/>
        </svg>
        816-552-4917
      </p>
      <p class="line">
        <svg viewBox="0 0 14 14" aria-hidden="true">
          <rect x="1" y="3" width="12" height="8" fill="var(--sky)"/>
          <polyline points="1,3 7,8 13,3" fill="none" stroke="var(--paper)" stroke-width="1.2"/>
        </svg>
        dfaulk@marlowhomesexample.com
      </p>
      <p class="license">Licensed in the State of Missouri</p>
    </div>
  </section>

</body>
</html>
```